Anzeigengestaltung für Verkauf & Installation von Alarmanlagen und Videoüberwachungssystemen
Zielgruppe
Verkauf und Installation von Alarmanlagen und Videoüberwachungssystemen.
Verkauf erfolgt über eigenen Onlineshop.
Installation der Anlagen im regionalen Umkreis, hauptsächlich Privatkunden.
Zielgruppe: Privatkunden, Familien, mit vorhandener Immobilie/Wohneigentum.
Aufgabenstellung
Zeitungsformat:
92 mm x 60 mm
s/w-4C
Text Entwurf als Orientierung befindet sich im Anhang, ebenso das Firmenlogo.
Bilder aus der Webseite sind ebenfalls beigefügt. Vielleicht lässt sich damit etwas anfangen, ich bin aber auch für Vorschläge aus geeigneten Stock-Bildern offen.

```html
<!DOCTYPE html>
<html lang="de">
<head>
<meta charset="utf-8">
<title>Wachwerk Sicherheit – Anzeige</title>
<link href="https://fonts.googleapis.com/css2?family=Oswald:wght@400;500&family=Lato:wght@400;700;900&display=swap" rel="stylesheet">
<style>
  :root {
    --page: #ffffff;
    --ad-light: #f3f3f3;
    --ad-mid: #e4e4e4;
    --accent: #d6402b;
    --ink: #2b2b2b;
    --ink-soft: #555555;
  }
  html, body {
    margin: 0;
    padding: 0;
    width: 756px;
    height: 1200px;
    overflow: hidden;
    background: var(--page);
  }
  .canvas {
    position: relative;
    width: 756px;
    height: 1200px;
  }
  .ad {
    position: absolute;
    left: 28px;
    top: 372px;
    width: 700px;
    height: 456px;
    box-sizing: border-box;
    border: 1px solid var(--accent);
    background: linear-gradient(160deg, var(--ad-light) 0%, var(--ad-mid) 55%, var(--ad-light) 100%);
    overflow: hidden;
    font-family: "Lato", sans-serif;
    color: var(--ink);
  }
  .ad__visuals {
    position: absolute;
    inset: 0;
    width: 100%;
    height: 100%;
  }
  .brand {
    position: absolute;
    left: 30px;
    top: 30px;
    display: flex;
    align-items: center;
    gap: 14px;
  }
  .brand__dot {
    width: 40px;
    height: 40px;
    border-radius: 50%;
    background: var(--accent);
  }
  .brand__name {
    font-family: "Lato", sans-serif;
    font-weight: 900;
    font-size: 28px;
    line-height: 1;
    color: var(--ink);
    letter-spacing: -0.3px;
  }
  .brand__claim {
    display: block;
    margin-top: 5px;
    font-weight: 700;
    font-size: 9px;
    color: var(--ink-soft);
    letter-spacing: 0.2px;
  }
  .headline {
    position: absolute;
    left: 28px;
    margin: 0;
    font-family: "Oswald", sans-serif;
    font-weight: 500;
    color: var(--accent);
    text-transform: uppercase;
    letter-spacing: 0.3px;
    line-height: 1;
  }
  .headline--product { top: 120px; font-size: 29px; }
  .headline--funding { top: 282px; font-size: 26px; }
  .benefits {
    position: absolute;
    left: 28px;
    top: 172px;
    margin: 0;
    padding: 0;
    list-style: none;
  }
  .benefits__item {
    display: flex;
    align-items: center;
    gap: 9px;
    height: 27px;
    font-size: 18px;
    font-weight: 700;
    color: var(--ink);
  }
  .benefits__tick { width: 15px; height: 15px; flex: none; }
  .services {
    position: absolute;
    left: 28px;
    top: 330px;
    display: flex;
    gap: 18px;
    align-items: center;
  }
  .services__item {
    display: flex;
    align-items: center;
    gap: 6px;
    font-family: "Oswald", sans-serif;
    font-size: 14px;
    color: var(--ink);
    text-transform: uppercase;
  }
  .services__icon { width: 26px; height: 24px; flex: none; }
  .contact {
    position: absolute;
    left: 28px;
    top: 393px;
    margin: 0;
    font-style: normal;
    font-size: 11.5px;
    font-weight: 700;
    line-height: 20px;
    color: var(--ink);
  }
  .contact__sep {
    display: inline-block;
    width: 5px;
    height: 5px;
    margin: 0 6px 1px;
    border-radius: 50%;
    background: var(--accent);
  }
</style>
</head>
<body>
<div class="canvas">
  <section class="ad" aria-label="Anzeige Wachwerk Sicherheit">
    <svg class="ad__visuals" viewBox="0 0 660 430" preserveAspectRatio="none" aria-hidden="false">
      <defs>
        <linearGradient id="roomTones" x1="0" y1="0" x2="1" y2="1">
          <stop offset="0" stop-color="#e9dfcf"/>
          <stop offset="0.5" stop-color="#c79a66"/>
          <stop offset="1" stop-color="#e6e2da"/>
        </linearGradient>
        <linearGradient id="phoneTones" x1="0" y1="0" x2="1" y2="1">
          <stop offset="0" stop-color="#e3e1de"/>
          <stop offset="0.55" stop-color="#b7aca3"/>
          <stop offset="1" stop-color="#d8b9a4"/>
        </linearGradient>
      </defs>
      <polygon class="frame-accent" points="503,0 519,0 392,128 378,126" fill="#d6402b"/>
      <polygon class="photo-room" role="img" aria-label="Foto: Wohnzimmer von oben mit Sofa, grünem Teppich und Holzboden" points="519,0 660,0 660,388 390,130" fill="url(#roomTones)"/>
      <polygon class="frame-accent" points="660,388 660,396 383,128 390,130" fill="#d6402b" opacity="0.9"/>
      <polygon class="frame-accent" points="440,222 452,222 335,345 322,340" fill="#d6402b"/>
      <polygon class="photo-phone" role="img" aria-label="Foto: Hand hält Smartphone mit Live-Kamerabild der Wohnung" points="452,222 590,360 520,430 360,430 322,345" fill="url(#phoneTones)"/>
      <rect x="372" y="285" width="140" height="17" fill="#2a2a2a"/>
      <text x="442" y="298" text-anchor="middle" font-family="Georgia, serif" font-weight="700" font-size="12" fill="#ffffff">Home Security</text>
    </svg>

    <header class="brand">
      <span class="brand__dot" aria-hidden="true"></span>
      <div>
        <span class="brand__name">Wachwerk Sicherheit</span>
        <span class="brand__claim">Schützen Sie sich und Ihr Eigentum</span>
      </div>
    </header>

    <h2 class="headline headline--product">Moderne Funkalarmanlagen</h2>

    <ul class="benefits">
      <li class="benefits__item"><svg class="benefits__tick" viewBox="0 0 16 16"><circle cx="8" cy="8" r="8" fill="#2b2b2b"/><path d="M4.3 8.3l2.4 2.4 5-5" stroke="#fff" stroke-width="2" fill="none"/></svg>Individuelle Beratung</li>
      <li class="benefits__item"><svg class="benefits__tick" viewBox="0 0 16 16"><circle cx="8" cy="8" r="8" fill="#2b2b2b"/><path d="M4.3 8.3l2.4 2.4 5-5" stroke="#fff" stroke-width="2" fill="none"/></svg>Onlineshop</li>
      <li class="benefits__item"><svg class="benefits__tick" viewBox="0 0 16 16"><circle cx="8" cy="8" r="8" fill="#2b2b2b"/><path d="M4.3 8.3l2.4 2.4 5-5" stroke="#fff" stroke-width="2" fill="none"/></svg>Installation</li>
    </ul>

    <h2 class="headline headline--funding">Landesförderung möglich</h2>

    <div class="services">
      <span class="services__item">
        <svg class="services__icon" viewBox="0 0 26 24"><path d="M7 20v-8a6 6 0 0 1 12 0v8z" fill="#d6402b"/><rect x="5" y="20" width="16" height="3" fill="#2b2b2b"/><path d="M13 1v3M3 5l2 2M23 5l-2 2M1 12h3M22 12h3" stroke="#2b2b2b" stroke-width="1.5"/><rect x="11.5" y="12" width="3" height="5" fill="#fff"/></svg>
        Alarm
      </span>
      <span class="services__item">
        <svg class="services__icon" viewBox="0 0 26 24"><path d="M2 7V2h5M19 2h5v5M24 17v5h-5M7 22H2v-5" stroke="#2b2b2b" stroke-width="2" fill="none"/><circle cx="13" cy="12" r="4" fill="#d6402b"/></svg>
        Video
      </span>
      <span class="services__item">
        <svg class="services__icon" viewBox="0 0 26 24"><path d="M1 11L8 4l7 7v9H1z" fill="none" stroke="#2b2b2b" stroke-width="1.8"/><rect x="13" y="7" width="11" height="16" rx="2" fill="#2b2b2b"/><rect x="15" y="9.5" width="7" height="10" fill="#d6402b"/></svg>
        Hausautomation
      </span>
    </div>

    <address class="contact">
      Lindenweg 12<span class="contact__sep"></span>74999 Musterfeld<span class="contact__sep"></span>07900-4821<br>
      www.wachwerk-sicherheit.de&nbsp; E-Mail: info@wachwerk-sicherheit.de
    </address>
  </section>
</div>
</body>
</html>
```